HM Quick Quote Screen

We are looking for two things:
1. On our main website (www.harborlinemutual.example) we would like to add a section for someone to enter their address and email address in return for a "quick quote."
2. Once they hit "enter" we would like a page built out that contains all the information that we would plug in from the backend.
We are an insurance company that focuses on property and powersports. This project in particular would focus on property (homeowner's specifically).
Reason: One of the decision makers will be out of the office until next week so we will provide our response next Tuesday. Thank you for your patience!
Insurance

```html
<!DOCTYPE html>
<html lang="en">
<head>
<meta charset="utf-8">
<title>Harborline Mutual – Quick Quote</title>
<link href="https://fonts.googleapis.com/css2?family=Arimo:wght@400;700&family=Gelasio:wght@400&display=swap" rel="stylesheet">
<style>
:root{
  --page-bg:#c5cad9;
  --frame:#eef0f4;
  --ink:#111111;
  --brand:#3b3878;
  --band-top:#fbfbfb;
  --band-bottom:#c9cbce;
  --ocean-dark:#2f4f7c;
  --ocean-mid:#45699a;
  --ocean-light:#6fa3bb;
  --card:#ffffff;
  --side-text:#dfe4ee;
  --divider:#c8d2e4;
  --field-border:#7a7a7a;
  --button:#2f5f93;
  --button-dark:#1a3556;
  --copy:#e9ecf2;
}
*{box-sizing:border-box;margin:0;padding:0}
html,body{width:1200px;height:845px;overflow:hidden}
body{background:var(--page-bg);font-family:"Arimo",Arial,sans-serif;color:var(--ink);position:relative}
.site{position:absolute;left:88px;top:6px;width:1027px;height:803px;background:var(--frame);border:1px solid #b8bcc6}
.masthead{position:absolute;left:1px;top:2px;width:1023px;height:112px;background:linear-gradient(#f2f2f2,#ffffff 20%,#ffffff 80%,#ececec)}
.brand{position:absolute;left:10px;top:52px;display:flex;align-items:center;gap:10px}
.brand-mark{width:22px;height:22px;border-radius:50%;background:var(--brand)}
.brand-name{font-family:"Gelasio",Georgia,serif;font-size:31px;color:var(--brand)}
.hotlines{position:absolute;right:12px;top:78px;text-align:right;font-weight:700;font-size:13.5px;line-height:16px}
.navbar{position:absolute;left:1px;top:114px;width:1023px;height:47px;background:linear-gradient(var(--band-top),#e9e9ea 60%,var(--band-bottom));border-top:1px solid #9a9a9a}
.tagline{position:absolute;left:60px;top:13px;font-size:18px;color:var(--brand);letter-spacing:-.3px}
.nav{position:absolute;left:398px;top:15px;display:flex;font-size:14.5px;letter-spacing:.2px}
.nav span{padding:0 13px;border-left:1px solid #6a4a8a;line-height:16px}
.nav span:first-child{border-left:none;padding-left:0}
.stage{position:absolute;left:1px;top:161px;width:1023px;height:604px;background:linear-gradient(100deg,var(--ocean-light) 0%,var(--ocean-mid) 35%,var(--ocean-dark) 75%,#395f8c 100%)}
.card{position:absolute;left:4px;top:9px;width:809px;height:552px;background:var(--card);border-radius:7px;box-shadow:4px 4px 0 rgba(20,30,50,.55)}
.card::after{content:"";position:absolute;left:0;right:0;bottom:0;height:38px;border-radius:0 0 7px 7px;background:linear-gradient(#ffffff,#b8c6d8)}
.card h1{position:absolute;left:15px;top:13px;font-family:"Gelasio",Georgia,serif;font-weight:400;font-size:20px;color:#333}
.intro{position:absolute;left:17px;top:49px;font-size:12px;color:#222}
.field{position:absolute;left:16px}
.field label{display:block;font-size:12px;font-weight:700;margin-bottom:6px}
.input{width:212px;height:22px;border:1px solid var(--field-border);background:#fff}
.enter{position:absolute;left:18px;top:475px;width:75px;height:30px;background:linear-gradient(var(--button),var(--button-dark));border:2px solid #0f2036;color:#fff;font-weight:700;font-style:italic;font-size:14px;line-height:26px;text-align:center}
.divider{position:absolute;left:825px;top:6px;width:2px;height:578px;background:var(--divider)}
.products{position:absolute;left:845px;top:22px;color:var(--side-text);font-weight:700}
.products h2{font-size:19px;color:#fff;margin-bottom:21px}
.group{margin-bottom:14px}
.group h3{font-weight:400;font-size:19px;color:#fff;line-height:22px}
.group p{font-size:15.5px;line-height:20px}
.rating{position:absolute;left:840px;top:432px;width:170px;text-align:center;color:var(--side-text);font-weight:700;font-size:13px;line-height:16px}
.seal{width:112px;height:40px;margin:0 auto 6px;border-radius:50%;background:linear-gradient(#d6d9df,#8a8f9a);border:2px solid #f4f4f4}
.social{position:absolute;left:434px;top:585px;color:#fff;font-size:16px;display:flex;align-items:center;gap:5px}
.social i{display:inline-block;width:14px;height:14px;background:#3a7fc6}
.footer{position:absolute;left:1px;top:765px;width:1023px;height:36px;background:linear-gradient(#d0d2d5,#ffffff 50%,#ececec);border-top:1px solid #8d8d8d}
.footer .nav{left:296px;top:12px}
.legal{position:absolute;left:0;width:1200px;top:826px;text-align:center;font-size:11.5px;color:var(--copy)}
</style>
</head>
<body>
<div class="site">
  <header class="masthead">
    <div class="brand"><span class="brand-mark"></span><span class="brand-name">Harborline Mutual</span></div>
    <div class="hotlines">Customer Service: (800) 555-0142<br>Claims: (800) 555-0187</div>
  </header>
  <div class="navbar">
    <div class="tagline">Smart Choice.</div>
    <nav class="nav"><span>Home</span><span>About Us</span><span>Producer Locator</span><span>Producer Login</span></nav>
  </div>
  <main class="stage">
    <section class="card">
      <h1>Quick Quote</h1>
      <p class="intro">Please fill the form and hit submit for a quick quote.</p>
      <div class="field" style="top:76px"><label>Your Full Name</label><div class="input"></div></div>
      <div class="field" style="top:126px"><label>Your Email id</label><div class="input"></div></div>
      <div class="field" style="top:178px"><label>Your Phone No</label><div class="input"></div></div>
      <div class="field" style="top:229px"><label>Your Address</label><div class="input" style="height:63px"></div></div>
      <div class="field" style="top:325px"><label>Your Requirements</label><div class="input" style="height:118px"></div></div>
      <div class="enter">ENTER</div>
    </section>
    <div class="divider"></div>
    <aside class="products">
      <h2>Our Products!</h2>
      <div class="group"><h3>Property</h3><p>Homeowners<br>Renters<br>Condominium<br>Manufactured Home</p></div>
      <div class="group"><h3>Powersports</h3><p>Motorcycle<br>Off-Road/ATV<br>Personal Watercraft<br>Pleasure Boat<br>Motorhome<br>Travel Trailer</p></div>
      <div class="group"><h3>Liability</h3><p>Umbrella</p></div>
    </aside>
    <div class="rating"><div class="seal"></div>Crestmark Rating of A<br>for financial strength<br>and stability.</div>
    <div class="social">Stay Connected: <i></i><i></i></div>
  </main>
  <footer class="footer">
    <nav class="nav"><span>Careers</span><span>Privacy Policy</span><span>Contact Us</span><span>Not a Producer?</span></nav>
  </footer>
</div>
<p class="legal">© 2010 Keller Insurance Services, P.O Box 218, Fairview, CA 90210. CA License 0472816 / National Producer No. 618204</p>
</body>
</html>
```